Stonebrook 720 Real Estate Investment Company

We need a business card designed for a real estate investment company named Stonebrook 720. We want to use red#f04a50, orange #f37122 and yellow #fbee3e as the color scheme. The logo colors will need to be modified from the current blue palette. I've attach VitaPathway logo example that captures the color scheme we're going for for Stonebrook 720. Looking for clean Sans Serif fonts.
Contact Information for Business Card
Daniel Furlow
Managing Partner
48317 Whitfield Lane, Suite 510
Tampa, FL 33718
813-555-4870 Mobile
dfurlow@stonebrook720.example
www.stonebrook720.example
Requirements
Must have
- Looking for creative responses.
Nice to have
- Must hit color palette... orange, red, yellow

```html
<!DOCTYPE html>
<html lang="en">
<head>
<meta charset="utf-8">
<title>Stonebrook 720 – Business Card</title>
<link rel="stylesheet" href="https://fonts.googleapis.com/css2?family=Lato:wght@400;700;900&display=swap">
<style>
  :root {
    --backdrop: #2b2b2b;
    --card: #1b1b1b;
    --red: #f04a50;
    --orange: #f37122;
    --yellow: #fbee3e;
    --ink: #f2f2f2;
    --rule: #6a6a6a;
  }
  * { box-sizing: border-box; margin: 0; padding: 0; }
  html, body {
    width: 1200px; height: 895px; overflow: hidden;
    background: var(--backdrop);
    font-family: "Lato", sans-serif;
  }
  .stage {
    width: 1200px; height: 895px;
    display: flex; flex-direction: column;
    align-items: center; justify-content: center; gap: 36px;
  }
  .card {
    width: 700px; height: 400px;
    background: var(--card);
    position: relative;
    box-shadow: 0 12px 30px rgba(0,0,0,.45);
  }
  .brand {
    display: flex; align-items: center; gap: 14px;
    color: var(--yellow);
    font-weight: 900;
    letter-spacing: .5px;
    white-space: nowrap;
  }
  .brand-dot {
    border-radius: 50%;
    background: var(--red);
    flex: none;
  }
  .card-front { display: flex; align-items: center; justify-content: center; }
  .card-front .brand { font-size: 56px; }
  .card-front .brand-dot { width: 34px; height: 34px; }

  .card-back .brand {
    position: absolute; left: 60px; top: 210px;
    font-size: 34px;
  }
  .card-back .brand-dot { width: 22px; height: 22px; }
  .divider {
    position: absolute; left: 440px; top: 70px;
    width: 1px; height: 260px; background: var(--rule);
  }
  .contact {
    position: absolute; left: 468px; top: 78px; width: 220px;
    color: var(--ink);
  }
  .contact-name { font-size: 24px; font-weight: 400; line-height: 1.1; }
  .contact-name .first { color: var(--yellow); }
  .contact-name .last { color: var(--red); }
  .contact-role { font-size: 13px; margin-top: 2px; }
  .contact-address { font-size: 13px; line-height: 1.45; margin-top: 18px; }
  .contact-lines { list-style: none; margin-top: 16px; font-size: 12.5px; line-height: 1.7; }
  .contact-lines li { display: flex; align-items: center; gap: 9px; }
  .contact-lines svg { width: 12px; height: 12px; flex: none; fill: var(--orange); }
</style>
</head>
<body>
<main class="stage">
  <section class="card card-front" aria-label="Card front">
    <div class="brand"><span class="brand-dot"></span>Stonebrook 720</div>
  </section>

  <section class="card card-back" aria-label="Card back">
    <div class="brand"><span class="brand-dot"></span>Stonebrook 720</div>
    <div class="divider"></div>
    <div class="contact">
      <p class="contact-name"><span class="first">DANIEL</span> <span class="last">FURLOW</span></p>
      <p class="contact-role">Managing Partner</p>
      <p class="contact-address">48317 Whitfield Lane<br>Suite 510, Tampa<br>FL 33718</p>
      <ul class="contact-lines">
        <li>
          <svg viewBox="0 0 24 24"><path d="M6.6 10.8a15.1 15.1 0 0 0 6.6 6.6l2.2-2.2a1 1 0 0 1 1-.25 11.4 11.4 0 0 0 3.6.57 1 1 0 0 1 1 1V20a1 1 0 0 1-1 1A17 17 0 0 1 3 4a1 1 0 0 1 1-1h3.5a1 1 0 0 1 1 1c0 1.25.2 2.45.57 3.57a1 1 0 0 1-.25 1z"/></svg>
          813-555-4870
        </li>
        <li>
          <svg viewBox="0 0 24 24"><path d="M2 5h20v14H2z M2 5l10 8 10-8" fill="none" stroke="#f37122" stroke-width="2.4"/></svg>
          dfurlow@stonebrook720.example
        </li>
        <li>
          <svg viewBox="0 0 24 24"><circle cx="12" cy="12" r="9.5" fill="none" stroke="#f37122" stroke-width="2"/><path d="M2.5 12h19M12 2.5c3 3 3 16 0 19M12 2.5c-3 3-3 16 0 19" fill="none" stroke="#f37122" stroke-width="1.6"/></svg>
          www.stonebrook720.example
        </li>
      </ul>
    </div>
  </section>
</main>
</body>
</html>
```